Stationary & Business Cards
TRB Weddings & Events by Greta
You need to extend the project before designers can submit more proposals, right now it is locked. Thank you! :)
And we need business cards, stationary & envelopes.
They like a zen feel...cherry blossoms...birds...
Thank you for all of your submissions. The owners do not like the purple logo anymore and have completly changed it. We have uploaded a eps file for it. This project is guaranteed and we will be picking a winner. If you have time please submit new designs. Thank you.
Your eps file is an image please upload orignal Ai file.
-Thanks
Please upload ai or eps of your logo.

```html
<!DOCTYPE html>
<html lang="en">
<head>
<meta charset="utf-8">
<title>TRB Weddings &amp; Events by Greta — Stationery</title>
<link href="https://fonts.googleapis.com/css2?family=Questrial&display=swap" rel="stylesheet">
<style>
  :root{
    --leaf:#a3cf3e;
    --leaf-soft:#c2e07a;
    --leaf-pale:rgba(163,207,62,0);
    --paper:#ffffff;
    --ink:#555555;
    --ink-soft:#8a8a8a;
    --shadow:rgba(0,0,0,.22);
  }
  *{margin:0;padding:0;box-sizing:border-box}
  html,body{width:1200px;height:751px;overflow:hidden;background:var(--paper)}
  body{position:relative;font-family:"Questrial",sans-serif;color:var(--ink)}

  .sheet{position:absolute;background:var(--paper);box-shadow:2px 3px 8px var(--shadow);overflow:hidden}
  .letterhead{left:36px;top:34px;width:511px;height:677px}
  .card-front{left:65px;top:192px;width:199px;height:122px}
  .card-back{left:65px;top:348px;width:199px;height:120px}
  .envelope-front{left:576px;top:163px;width:600px;height:202px}
  .envelope-back{left:576px;top:446px;width:600px;height:254px}

  .ornament{position:absolute}
  .ornament.top-left{left:0;top:0;clip-path:polygon(0 0,100% 0,0 100%);
    background:linear-gradient(135deg,var(--leaf) 0%,var(--leaf-soft) 45%,var(--leaf-pale) 90%)}
  .ornament.bottom-right{right:0;bottom:0;clip-path:polygon(100% 0,100% 100%,0 100%);
    background:linear-gradient(315deg,var(--leaf) 0%,var(--leaf-soft) 45%,var(--leaf-pale) 90%)}

  .lockup{position:absolute;display:flex;align-items:center;gap:6px;white-space:nowrap;transform:translateX(-50%);color:var(--ink)}
  .lockup-square{flex:none;background:var(--leaf)}
  .lockup.on-flap{color:var(--paper)}
  .lockup.on-flap .lockup-square{background:var(--paper)}

  .footer-lines{position:absolute;left:0;width:100%;text-align:center;font-size:9px;color:var(--ink-soft);line-height:15px}

  .contact{position:absolute;left:96px;top:30px;color:var(--ink);font-size:6px;line-height:8px}
  .contact .person{font-size:9px;line-height:11px}
  .contact .role{color:var(--ink-soft);margin-bottom:10px}
  .contact .detail{color:var(--ink-soft)}

  .return-line{position:absolute;font-size:6px;color:var(--ink-soft);transform:translateX(-50%);white-space:nowrap}
  .flap{position:absolute;left:0;top:0}
</style>
</head>
<body>

<section class="sheet letterhead" aria-label="Letterhead">
  <div class="ornament top-left" style="width:70px;height:165px" role="img" aria-label="Green floral corner ornament"></div>
  <div class="ornament bottom-right" style="width:70px;height:165px" role="img" aria-label="Green floral corner ornament"></div>
  <div class="lockup" style="left:255px;top:100px;font-size:13px">
    <span class="lockup-square" style="width:14px;height:14px"></span>
    <span>TRB Weddings &amp; Events by Greta</span>
  </div>
  <div class="footer-lines" style="top:626px">
    <div>Seaview Cove, CA | Phone: 714.555.0182</div>
    <div>www.trbweddingsandevents.com</div>
  </div>
</section>

<section class="sheet card-front" aria-label="Business card front">
  <div class="ornament top-left" style="width:40px;height:70px" role="img" aria-label="Green floral corner ornament"></div>
  <div class="ornament bottom-right" style="width:36px;height:55px" role="img" aria-label="Green floral corner ornament"></div>
  <div class="lockup" style="left:100px;top:55px;font-size:7px;gap:4px">
    <span class="lockup-square" style="width:8px;height:8px"></span>
    <span>TRB Weddings &amp; Events by Greta</span>
  </div>
</section>

<section class="sheet card-back" aria-label="Business card back">
  <div class="ornament top-left" style="width:40px;height:70px" role="img" aria-label="Green floral corner ornament"></div>
  <div class="ornament bottom-right" style="width:30px;height:45px" role="img" aria-label="Green floral corner ornament"></div>
  <div class="contact">
    <div class="person">Greta Halvorsen</div>
    <div class="role">Event Consultant</div>
    <div class="detail">Seaview Cove, CA</div>
    <div class="detail">714.555.0182</div>
    <div class="detail">greta@trbweddingsandevents.com</div>
    <div class="detail">www.trbweddingsandevents.com</div>
  </div>
</section>

<section class="sheet envelope-front" aria-label="Envelope front">
  <div class="ornament top-left" style="width:55px;height:95px" role="img" aria-label="Green floral corner ornament"></div>
  <div class="ornament bottom-right" style="width:42px;height:70px" role="img" aria-label="Green floral corner ornament"></div>
  <div class="lockup" style="left:125px;top:64px;font-size:8px;gap:4px">
    <span class="lockup-square" style="width:9px;height:9px"></span>
    <span>TRB Weddings &amp; Events by Greta</span>
  </div>
  <div class="return-line" style="left:125px;top:80px">Seaview Cove, CA</div>
</section>

<section class="sheet envelope-back" aria-label="Envelope back">
  <svg class="flap" width="600" height="120" viewBox="0 0 600 120" aria-hidden="true">
    <path d="M0 0 H600 V74 Q600 94 578 96 L322 116 Q300 118 278 116 L22 96 Q0 94 0 74 Z" fill="var(--leaf)"/>
  </svg>
  <div class="lockup on-flap" style="left:300px;top:44px;font-size:9px;gap:5px">
    <span class="lockup-square" style="width:9px;height:9px"></span>
    <span>TRB Weddings &amp; Events by Greta</span>
  </div>
</section>

</body>
</html>
```